New design for a physiotherapy clinic specializing in laser therapy

BrightPath Physiotherapy is a unique clinic specializing in laser therapy. The clinic is now 7 years old and has a well established reputation for patient care.

We are the largest laser physiotherapy clinic in Mississauga, ON, Canada. We use state of the art laser therapy equipment. Our knowledge base of how to use Low Level Laser Therapy in conjunction with traditional physiotherapy is what sets us apart. Nobody wants to live with pain and everyone wants to get better as quickly as possible. Our treatment methodology helps our patients return to normal lives quickly.

We want a website that communicates expertise, trust and shows that we care for our patients. We also want people to understand that the treatments are painless and speed up healing naturally.
Updates

Please include a location tab in your submission.  This page should have a map of our location and our phone number.

I do not want any white coat and stethoscope people. We do not see hospitalized patients. We use Zorva-Kel NuvaQuill laser web site www.nuvaquilllaser.example please remove any images with other laser machines. I do not want "massage" therapy pictures as the main image. We treat post op total hip and knee replacements, rotator cuff injuries, osteoarthritic back pain patients, sprained ankles, degenerative disc disease problems as some of the more general injuries seen.

Industry/Entity Type

Clinic

Requirements
Must have
• We want to retain as much of the current content as possible. We will be looking at editing the content to make it shorter.

In addition to the current pages we want to add a blog page and link.

see our current site www.brightpathphysio.example
Nice to have
• Medical Images in the Whiplash and Auto Injuries should be re-drawn.

We want a clean, uncluttered look to the site.

Should not have
• Do not use illustrations of lasers shooting out or cutting. This is a "Cold" laser and does not cut. The laser procedure is gentle and soothing.

```html
<!DOCTYPE html>
<html lang="en">
<head>
<meta charset="utf-8">
<title>BrightPath Physiotherapy</title>
<link href="https://fonts.googleapis.com/css2?family=Roboto:wght@300;400;500&display=swap" rel="stylesheet">
<style>
:root{
  --green:#3f9a0e;
  --green-bright:#5cb52a;
  --green-text:#4a9a1c;
  --ink:#1f1f1f;
  --body:#555;
  --muted:#777;
  --paper:#efefef;
  --white:#fff;
}
*{margin:0;padding:0;box-sizing:border-box}
html,body{width:930px;height:1200px;overflow:hidden}
body{font-family:'Roboto',Arial,sans-serif;background:var(--white);color:var(--ink);position:relative}
a{color:inherit;text-decoration:none}
.wrap{position:absolute;left:128px;width:674px}

/* header */
.site-header{position:absolute;top:0;left:0;width:930px;height:72px;background:linear-gradient(#f6faf3,#e4efdc)}
.brand{position:absolute;left:130px;top:26px;display:flex;align-items:center;gap:8px}
.brand-dot{width:12px;height:12px;border-radius:50%;background:var(--green-bright)}
.brand-name{font-size:18px;font-weight:400;color:#333;letter-spacing:.5px}
.util-nav{position:absolute;right:130px;top:15px;font-size:7.5px;color:#666}
.util-nav span{margin:0 4px;color:#aaa}
.main-nav{position:absolute;right:130px;top:43px;display:flex;gap:11px;font-size:9.3px;font-weight:500;color:#222}
.main-nav .active{color:var(--green-bright)}

/* hero */
.hero{position:absolute;top:72px;left:0;width:930px;height:270px;background:var(--green)}
.hero-photo{position:absolute;left:128px;top:0;width:674px;height:270px;background:linear-gradient(90deg,#c9e3b8 0%,#eef3ef 25%,#e6cdb8 55%,#f1f2f2 80%,#d0e6c2 100%)}
.hero-arrow{position:absolute;top:115px;width:24px;height:36px;background:rgba(255,255,255,.55);display:flex;align-items:center;justify-content:center}
.hero-arrow.prev{left:105px}.hero-arrow.next{left:802px}

/* commitment */
.commitment{position:absolute;top:342px;left:0;width:930px;height:293px;background:var(--paper);border-bottom:1px solid #ddd}
.commitment h1{position:absolute;top:35px;width:930px;text-align:center;font-size:31px;font-weight:500;color:var(--green-bright)}
.commitment p{position:absolute;top:72px;width:930px;text-align:center;font-size:15.5px;font-weight:300;color:#444}
.services{top:129px;display:flex;gap:2px}
.service{width:167px}
.service-img{height:99px}
.service h3{font-size:8.5px;font-weight:500;text-align:center;margin-top:11px;letter-spacing:.2px;color:#333}

/* about */
.about{position:absolute;top:635px;left:0;width:930px;height:310px;overflow:hidden}
.about-bg{position:absolute;inset:0;background:linear-gradient(100deg,#eef0ea 0%,#f7f4f1 40%,#f0e4dc 65%,#eeeeec 100%)}
.col{position:absolute;top:56px;width:325px}
.col.left{left:128px}.col.right{left:478px}
.col h2{display:flex;align-items:center;gap:8px;font-size:17px;font-weight:500;color:var(--green-text);margin-bottom:22px}
.col p{font-size:9.3px;line-height:13.2px;color:var(--body);margin-bottom:13px}

/* contact */
.contact{position:absolute;top:945px;left:0;width:930px;height:168px;background:var(--green);color:var(--white)}
.contact h2{position:absolute;top:28px;width:930px;text-align:center;font-size:21px;font-weight:400;letter-spacing:.5px}
.contact-col{position:absolute;top:90px}
.contact-col h4{font-size:10.5px;font-weight:500;color:#17380a;margin-bottom:6px}
.contact-row{display:flex;gap:10px;align-items:flex-start}
.phones{font-size:11px;font-weight:500;line-height:16px}
.small{font-size:8.3px;line-height:10.5px}

/* footer */
.site-footer{position:absolute;top:1113px;left:0;width:930px;height:87px;background:var(--white)}
.foot-links{position:absolute;left:127px;top:33px;font-size:8.5px;line-height:13px;color:#555;width:480px}
.foot-links span{margin:0 3px;color:#aaa}
.foot-brand{position:absolute;left:716px;top:36px;display:flex;align-items:center;gap:5px}
.foot-brand .brand-dot{width:7px;height:7px}
.foot-brand .brand-name{font-size:10px}
</style>
</head>
<body>

<header class="site-header">
  <div class="brand"><span class="brand-dot"></span><span class="brand-name">BrightPath</span></div>
  <nav class="util-nav">FAQ's<span>|</span>Patient Forms<span>|</span>Employment Opportunities<span>|</span>Testimonials<span>|</span>Clinic Hours<span>|</span>Contact Us</nav>
  <nav class="main-nav">
    <a>PHYSIOTHERAPY</a><a>LASER THERAPY</a><a class="active">INSURANCE</a><a>WHIPLASH &amp; AUTO INJURIES</a><a>NEWS</a><a>MASSAGE THERAPY</a>
  </nav>
</header>

<section class="hero">
  <div class="hero-photo" role="img" aria-label="Therapist's hands resting on a patient's knee"></div>
  <a class="hero-arrow prev"><svg width="8" height="14" viewBox="0 0 8 14"><path d="M7 1L1 7l6 6" fill="none" stroke="#fff" stroke-width="1.6"/></svg></a>
  <a class="hero-arrow next"><svg width="8" height="14" viewBox="0 0 8 14"><path d="M1 1l6 6-6 6" fill="none" stroke="#fff" stroke-width="1.6"/></svg></a>
</section>

<section class="commitment">
  <h1>OUR PATIENT COMMITMENT</h1>
  <p>BrightPath Physiotherapy is committed to helping you get better, faster, with fewer treatments.</p>
  <div class="wrap services">
    <div class="service"><div class="service-img" role="img" aria-label="Hand holding a sore neck" style="background:linear-gradient(135deg,#c9b3a6,#e9d8cd 60%,#e8c24a)"></div><h3>WHIPLASH &amp; AUTO INJURIES</h3></div>
    <div class="service"><div class="service-img" role="img" aria-label="Cold laser applied to a leg" style="background:linear-gradient(135deg,#9a9896,#e9b483 50%,#d99a5f 85%,#3b4c9a)"></div><h3>LASER THERAPY</h3></div>
    <div class="service"><div class="service-img" role="img" aria-label="Therapist mobilizing a patient's arm" style="background:linear-gradient(135deg,#d9cfc8,#e8c9b4 50%,#f2efee)"></div><h3>PHYSIOTHERAPY</h3></div>
    <div class="service"><div class="service-img" role="img" aria-label="Hot stone massage" style="background:linear-gradient(135deg,#b86a2a,#e3a671 45%,#f3ebe5 85%)"></div><h3>MASSAGE THERAPY</h3></div>
  </div>
</section>

<section class="about">
  <div class="about-bg" role="img" aria-label="Faded photo of a patient receiving treatment"></div>
  <div class="col left">
    <h2><svg width="16" height="16" viewBox="0 0 16 16"><path d="M4 15V8L2 5.5 3 4.8 5 7V2h1.3v5V1h1.4v6V1.8H9V7V3h1.3v7L12.5 7.5l1 .8L10 15z" fill="#333"/></svg>WHO ARE WE</h2>
    <p>We are Mississauga's premier physiotherapy and low intensity laser therapy specialists. We integrate low intensity laser therapy (laser therapy or cold laser therapy) with physiotherapy to safely and effectively treat a wide variety of musculoskeletal injuries and inflammatory conditions (i.e. back pain, arthritis, knee injuries, shoulder injuries, tendonitis, bursitis, repetitive strains, auto &amp; sports injuries). This clinically proven program can achieve remarkable results for acute injury and chronic pain patients and is painless.</p>
    <p>We Use a multi-faceted regime of clinically tested and proven protocols with one goal in mind: Get you better, faster. Our results-focused team includes registered physiotherapists, registered massage therapists, certified kinesiologists and certified athletic therapists.</p>
  </div>
  <div class="col right">
    <h2><svg width="20" height="20" viewBox="0 0 20 20" fill="none" stroke="#333" stroke-width="1.3"><circle cx="10" cy="10" r="5.5"/><circle cx="10" cy="10" r="1.6"/><path d="M10 1v4M10 15v4M1 10h4M15 10h4M3.6 3.6l2.8 2.8M13.6 13.6l2.8 2.8M3.6 16.4l2.8-2.8M13.6 6.4l2.8-2.8"/></svg>UNIQUE TREATMENT APPROACH</h2>
    <p>When we combine laser therapy with traditional physiotherapy mobilization and strengthening, the results are remarkable.</p>
    <p>Low Intensity Laser Therapy (LILT), also know as biophotostimulation, helps restore normal cellular function while enhancing the body's natural healing processes. The laser treatments are painless. Frequently, patients will experience a reduction in pain after their first treatment and sleep more soundly that evening. At BrightPath, we use the NuvaQuill Professional Laser Therapy System exclusively. The NuvaQuill system was developed by a Canadian surgeon, Dr. Elias Morrow, and is the most sophisticated laser therapy system available. All treatments with the NuvaQuill system uses three stages, each stage has a different wavelength of light and different dosage.</p>
  </div>
</section>

<section class="contact">
  <h2>CONTACT INFORMATION</h2>
  <div class="contact-col" style="left:128px">
    <h4>Contact No.</h4>
    <div class="contact-row">
      <svg width="16" height="20" viewBox="0 0 16 20"><path d="M4 1l3 4-2 2c1 3 3 5 5 7l2-2 3 3-2 3C7 17 1 10 2 3z" fill="#fff"/></svg>
      <div class="phones">905-555-0142<br>905-555-0187</div>
    </div>
  </div>
  <div class="contact-col" style="left:320px">
    <h4>Clinic Hours</h4>
    <div class="contact-row">
      <svg width="18" height="18" viewBox="0 0 18 18" fill="none" stroke="#fff" stroke-width="1.2"><circle cx="9" cy="10" r="7"/><path d="M9 6v4l3 2M7 1.5h4"/></svg>
      <div class="small">Monday, Wednesday &amp; Friday 9 am to 6 pm<br>Tuesday &amp; Thursday 11 am to 7 pm<br>Saturday 9 am to 12 pm</div>
    </div>
  </div>
  <div class="contact-col" style="left:568px">
    <h4>Location:</h4>
    <div class="contact-row">
      <svg width="12" height="18" viewBox="0 0 12 18"><circle cx="6" cy="5" r="3.5" fill="none" stroke="#fff" stroke-width="1.3"/><path d="M6 8.5V15M2 16h8" stroke="#fff" stroke-width="1.3"/></svg>
      <div class="small">Harlow Centre, 4410 Brookvale Parkway, Mississauga, ON<br>L5X 2Q4 One block north of Highway 9 on Brookvale Parkway<br>We are located in the lower level of the mall, by the library</div>
    </div>
  </div>
</section>

<footer class="site-footer">
  <nav class="foot-links">Physiotherapy<span>|</span>Laser Therapy<span>|</span>Insurance<span>|</span>Whiplash &amp; Auto Injuries<span>|</span>News<span>|</span>Massage Therapy<span> </span>FAQ's<span>|</span>Patient Forms<br>Employment Opportunities<span>|</span>Testimonials<span>|</span>Clinic Hours<span>|</span>Contact Us</nav>
  <div class="foot-brand"><span class="brand-dot"></span><span class="brand-name">BrightPath</span></div>
</footer>

</body>
</html>
```